Looking for updated Letterhead and Compliments Slips to go with our new updated logo. This stationary will be used for letters to suppliers and customers so needs to be practical while also quite classic.

We are an engineering company so needs to be clean and precise

Target Market(s)

SME'S and large automotive customers

Industry/Entity Type

Automotive

Font styles to use
Sans Serif

Colors
85acd3
0356a4
0792cd
33a6d7
85abd2
ffffff

Requirements
Must have
• Address details as below
• KT Fabrications Limited
• Marbury Close
• Ellbridge
• Westvale
• DN47 3XP, UK
• Telephone: +44 (0)1632 960418
• Fax: +44 (0)1632 960735
• Email: sales@ktfabrications.example
• Web: www.ktfabrications.example
Nice to have
• Nice to have some element of being a British Manufacturer

```html
<!DOCTYPE html>
<html lang="en">
<head>
<meta charset="utf-8">
<title>KT Fabrications – Stationery</title>
<link href="https://fonts.googleapis.com/css2?family=Montserrat:wght@500;600&family=Open+Sans:wght@400;600&family=Great+Vibes&display=swap" rel="stylesheet">
<style>
:root{
  --navy:#0356a4;
  --sky:#85acd3;
  --cyan:#0792cd;
  --ink:#111111;
  --paper:#ffffff;
  --ghost:#eef1f8;
  --stage:#2e2622;
  --badge:#d62a2a;
}
*{margin:0;padding:0;box-sizing:border-box}
html,body{width:1200px;height:818px;overflow:hidden;background:var(--stage)}
body{position:relative;font-family:"Open Sans",sans-serif;color:#333}
.sheet{position:absolute;background:var(--paper);overflow:hidden;box-shadow:0 3px 10px rgba(0,0,0,.45)}
.sheet svg.swoosh{position:absolute;left:0;bottom:0;width:100%;display:block}
.wordmark{position:absolute;font-family:"Montserrat",sans-serif;font-weight:600;color:var(--navy);letter-spacing:.28em;white-space:nowrap;text-align:center;transform:translateX(-50%)}
.wordmark .dot{display:block;margin:0 auto 8px;border:2px solid var(--navy);border-radius:50%}
.script{position:absolute;font-family:"Great Vibes",cursive;white-space:nowrap;line-height:1}
.address,.contacts,.web{position:absolute;white-space:nowrap;line-height:1.55}
.address b{font-weight:600}
.label{position:absolute;font-family:"Open Sans",sans-serif;font-weight:600;color:#fff;font-size:14px}

/* letterhead */
.letterhead{left:57px;top:77px;width:484px;height:626px}
.letterhead .ring{position:absolute;left:167px;top:266px;width:142px;height:142px;border:27px solid var(--ghost);border-radius:50%}
.letterhead .foot{color:#fff;font-size:7.4px}

/* business card */
.card-front{left:634px;top:70px;width:199px;height:113px}
.card-front .holder{position:absolute;left:0;width:100%;top:56px;text-align:center;font-size:6px;color:#444;line-height:1}
.card-front .holder span{color:#888;font-size:4.4px}
.card-front .foot{color:#fff;font-size:4.4px}
.card-back{left:857px;top:71px;width:199px;height:113px}
.card-back .seal{position:absolute;left:104px;top:28px;width:38px;height:38px;border-radius:50%;background:var(--badge)}

/* compliment slips */
.slip-a{left:573px;top:214px;width:554px;height:249px}
.slip-a .foot{color:#fff;font-size:7.4px}
.slip-b{left:570px;top:483px;width:554px;height:249px}
.slip-b .band{position:absolute;left:0;top:0;width:100%;height:118px;background:var(--sky)}
.slip-b .rule{position:absolute;left:140px;top:202px;width:1px;height:30px;background:var(--navy)}
.slip-b .address,.slip-b .contacts{font-size:7.4px;color:#333}
.ico{color:var(--navy);display:inline-block;width:10px}
</style>
</head>
<body>

<!-- Letterhead -->
<section class="sheet letterhead">
  <div class="wordmark" style="left:242px;top:92px;font-size:15px"><i class="dot" style="width:22px;height:22px"></i>KT FABRICATIONS</div>
  <div class="ring" aria-hidden="true"></div>
  <svg class="swoosh" viewBox="0 0 484 200" height="200" aria-hidden="true">
    <path d="M0,85 C150,132 300,148 390,146 C300,152 120,134 0,100 Z" fill="var(--ink)"/>
    <path d="M0,101 C150,146 330,160 484,133 L484,200 L0,200 Z" fill="var(--navy)"/>
  </svg>
  <div class="address foot" style="left:37px;top:581px"><b>KT Fabrications Limited,</b><br>Marbury Close, Ellbridge<br>Westvale, DN47 3XP, UK</div>
  <div class="contacts foot" style="left:155px;top:581px">&#9990; +44 (0)1632 960418<br>&#9993; +44 (0)1632 960735<br>@ sales@ktfabrications.example</div>
  <div class="wordmark foot" style="left:414px;top:590px;font-size:7px;color:#fff">KT FABRICATIONS</div>
  <div class="web foot" style="right:34px;top:601px;font-weight:600;letter-spacing:.05em">www.ktfabrications.example</div>
</section>

<!-- Business card front -->
<section class="sheet card-front">
  <div class="wordmark" style="left:100px;top:16px;font-size:7px"><i class="dot" style="width:12px;height:12px;margin-bottom:5px"></i>KT FABRICATIONS</div>
  <div class="holder">Name Here <span>| Designation</span></div>
  <svg class="swoosh" viewBox="0 0 199 60" height="60" aria-hidden="true">
    <path d="M0,1 C50,18 110,26 165,25 C110,28 50,22 0,8 Z" fill="var(--ink)"/>
    <path d="M0,7 C60,28 140,30 199,20 L199,60 L0,60 Z" fill="var(--navy)"/>
  </svg>
  <div class="address foot" style="left:11px;top:87px"><b>KT Fabrications Limited,</b><br>Marbury Close, Ellbridge<br>Westvale, DN47 3XP, UK</div>
  <div style="position:absolute;left:101px;top:88px;width:1px;height:20px;background:#fff"></div>
  <div class="contacts foot" style="left:126px;top:87px">+44 (0)1632 960418<br>+44 (0)1632 960735<br>sales@ktfabrications.example</div>
</section>

<div class="label" style="left:856px;top:49px">Back Option 1</div>
<section class="sheet card-back">
  <div class="wordmark" style="left:62px;top:44px;font-size:5px;letter-spacing:.2em">KT FABRICATIONS</div>
  <div class="seal" role="img" aria-label="British manufacturer badge"></div>
  <div class="web" style="left:0;width:100%;top:86px;text-align:center;font-size:5px;color:var(--navy);letter-spacing:.1em">www.ktfabrications.example</div>
</section>

<!-- Compliment slip, option 1 -->
<section class="sheet slip-a">
  <div class="script" style="left:23px;top:22px;font-size:40px;color:var(--sky)">With Compliments...</div>
  <div class="wordmark" style="left:416px;top:70px;font-size:15px"><i class="dot" style="width:22px;height:22px"></i>KT FABRICATIONS</div>
  <svg class="swoosh" viewBox="0 0 554 249" height="249" aria-hidden="true">
    <path d="M0,146 C170,200 360,222 466,210 C360,226 150,206 0,162 Z" fill="var(--ink)"/>
    <path d="M0,162 C170,214 390,226 554,202 L554,249 L0,249 Z" fill="var(--navy)"/>
  </svg>
  <div class="address foot" style="left:18px;top:206px"><b>KT Fabrications Limited,</b><br>Marbury Close, Ellbridge, Westvale, DN47 3XP, UK</div>
  <div class="contacts foot" style="left:18px;top:229px">T: +44 (0)1632 960418,&nbsp; F: +44 (0)1632 960735,&nbsp; E: sales@ktfabrications.example</div>
  <div class="web foot" style="right:34px;top:229px;font-weight:600">www.ktfabrications.example</div>
</section>

<!-- Compliment slip, option 2 -->
<section class="sheet slip-b">
  <div class="band"></div>
  <div class="script" style="left:22px;top:24px;font-size:40px;color:#fff">With Compliments...</div>
  <div class="address" style="left:22px;top:200px"><b>KT Fabrications Limited,</b><br>Marbury Close, Ellbridge<br>Westvale, DN47 3XP, UK</div>
  <div class="rule"></div>
  <div class="contacts" style="left:155px;top:200px"><span class="ico">&#9990;</span>+44 (0)1632 960418<br><span class="ico">&#9993;</span>+44 (0)1632 960735<br><span class="ico">@</span>sales@ktfabrications.example</div>
  <div class="wordmark" style="left:432px;top:176px;font-size:15px"><i class="dot" style="width:22px;height:22px"></i>KT FABRICATIONS</div>
</section>
<div class="label" style="left:1066px;top:740px">Option 2</div>

</body>
</html>
```